依頼概要
■ 依頼の目的/概要
弊社の新商品を展示会で紹介するためのポスターを作成して頂きたいです。

新製品の製品名は『Plim!』というコンクリート塀です。

通常、家の周りに設置する塀は空洞ブロックを積上げて構築しますが、新製品『Plim!』はこれを一体化した構造で工場で製造する1枚の大きなコンクリート塀です。

従来の空洞ブロック積上げ式のブロック塀では地震時の損壊・転倒による人災が多数発生しています。
従来の塀は材料が安価なため利用されていますが、施工基準に基づかない方法で安易に構築されるケースも多いのが実状です。
鉄筋挿入部のコンクリートの充填もルーズになりがちなため、鉄筋の酸化によりブロック塀の劣化も早くなります。
また、土圧を支えきれないと思われる擁壁としての使用も多く見受けられます。
そのため、地震時のみならず、平常時においてもブロック塀の傾き・転倒等の危険な状況が多く発生しています。

今回の新製品では弊社工場内での厳格な設計基準、検査基準、安定計算の下で一体化された製品を使用するため、躯体の劣化、破損、転倒を防止することができ、平常時、地震時においても人災を免れることが可能となります。

イメージは添付の図を参照願います。
製品の断面図は添付のCADデータをご使用下さい。

■ 依頼詳細
・サイズ : A0 縦 のポスター作成をお願いします。
・使用フォント : Illustrator CS標準の小塚フォント及びTypeKitでダウンロード可能なフォントでアウトライン化していないデータ
・印刷プリンター : グランベストミラー plotMax R730 36インチ
印刷可能範囲 周囲5mm除外した内側
展示会準備の関係上、募集の締め切りを7日までとさせて頂きます。
ご了承願います。
イラストレータのバージョンを依頼文中でCSと記載しておりますが、
CSではなく“CC”でした。
大変失礼いたしました。
CCのバージョンでご対応をお願いいたします。
CADが開けない方からのご連絡を頂きましたので、イラストレータで製品形状のデータを添付させていただきます。
よろしくお願いいたします。
・新製品『Plim!』の施工イメージ図 (Plim_H1500フェンス無し)
・従来のブロック塀の正常施工写真 (ブロック塀 正常1)
以上2点を素材として追加で添付いたします。

ポスターのイメージですが、
新製品の”安全性”が際立つポスターにして頂ければと思います。
また、展示会用なのでパッと目にとまるような目立つポスターが希望です。

よろしくお願いいたします。
■ 選んだ理由

とても目立ち、人目を引くデザインである点、商品名や製品イメージ(従来品、新製品)が大きくてわかりやすい点を評価し当選とさせて頂きました。

■ 提案者全員のお礼・コメント

短納期の依頼でしたのに多くのご提案頂きありがとうございました。
手書きの添付資料から製品のウリを掴みポスターを作成頂きましたこと、大変感謝しております。
今後もコンクリート関連製品に関する依頼をしていく予定がございますので、是非またご提案を頂ければ幸いです。
よろしくお願いいたします。

```html
<!DOCTYPE html>
<html lang="ja">
<head>
<meta charset="utf-8">
<title>Plim! まったく新しいコンクリート塀</title>
<link rel="stylesheet" href="https://fonts.googleapis.com/css2?family=Noto+Sans+JP:wght@400;700;900&display=swap">
<style>
:root{
  --blue:#1f58bd;
  --green:#6cb72f;
  --green-pale:#e6f3d6;
  --pink:#e0407e;
  --navy:#1b2c4a;
  --white:#ffffff;
  --text:#2b2b2b;
  --red:#d9262d;
}
*{margin:0;padding:0;box-sizing:border-box}
html,body{width:849px;height:1200px;overflow:hidden;background:#fff}
body{font-family:"Noto Sans JP",sans-serif;color:var(--text)}
.poster{position:relative;width:849px;height:1200px;overflow:hidden;background:#f4f7f2}
.hero-photo{position:absolute;left:0;top:0;width:849px;height:615px;
  background:linear-gradient(160deg,#9fb3c4 0%,#7f8f98 35%,#5f6a6e 65%,#3e474c 100%)}
.hero-shade{position:absolute;left:0;top:0;width:849px;height:615px;
  background:linear-gradient(90deg,rgba(20,30,50,.35) 0%,rgba(20,30,50,.05) 60%,rgba(20,30,50,.25) 100%)}
.tagline{position:absolute;left:18px;top:14px;background:var(--green);color:var(--white);
  font-weight:700;font-size:22px;padding:4px 14px;letter-spacing:1px}
.product-name{position:absolute;left:28px;top:58px;font-weight:900;font-size:150px;line-height:1;
  color:var(--blue);letter-spacing:2px}
.new-badge{position:absolute;left:300px;top:118px;width:92px;height:92px;border-radius:50%;
  background:var(--green);color:var(--white);font-weight:900;font-size:24px;line-height:1.05;
  display:flex;align-items:center;justify-content:center;text-align:center;transform:rotate(-12deg)}
.headline{position:absolute;right:22px;top:18px;writing-mode:vertical-rl;color:var(--white);
  font-weight:900;font-size:36px;line-height:1.3;letter-spacing:2px;height:560px;
  text-shadow:0 2px 6px rgba(0,0,0,.45)}
.intro{position:absolute;left:34px;top:250px;width:500px;color:var(--white);font-weight:700;
  font-size:16.5px;line-height:1.65;text-shadow:0 1px 4px rgba(0,0,0,.6)}
.intro em{font-style:normal;color:#ffe14a}
.issues-title{position:absolute;left:34px;top:356px;color:var(--white);font-weight:700;font-size:17px;
  text-shadow:0 1px 4px rgba(0,0,0,.6)}
.issues{position:absolute;left:34px;top:388px;width:470px;list-style:none}
.issue{display:flex;align-items:center;gap:10px;background:rgba(20,28,45,.72);margin-bottom:6px;
  padding:6px 10px;height:40px;border-radius:3px}
.issue-num{flex:none;width:30px;height:30px;border-radius:50%;background:var(--pink);color:var(--white);
  font-weight:900;font-size:17px;display:flex;align-items:center;justify-content:center}
.issue-text{color:#ffd0e0;font-size:11px;line-height:1.4;font-weight:700}
.solution-band{position:absolute;left:0;top:628px;width:849px;height:44px;background:var(--green);
  color:var(--white);font-weight:900;font-size:22px;display:flex;align-items:center;justify-content:center;letter-spacing:1px}
.solution-panel{position:absolute;left:24px;top:684px;width:801px;height:496px;background:var(--white);
  border:3px solid var(--green);border-radius:6px}
.solution-text{position:absolute;left:22px;top:14px;width:757px;font-size:12px;line-height:1.6;font-weight:700}
.method-label{position:absolute;width:74px;height:74px;border-radius:50%;display:flex;align-items:center;
  justify-content:center;text-align:center;font-weight:900;font-size:14px;line-height:1.2}
.method-label.old{left:26px;top:110px;background:var(--green-pale);color:var(--navy);border:2px solid var(--navy)}
.method-label.new{left:520px;top:95px;width:110px;height:110px;background:var(--pink);color:var(--white);font-size:14px}
.diagram{position:absolute;border-radius:4px}
.diagram.old{left:110px;top:90px;width:210px;height:340px;background:linear-gradient(180deg,#eef2f5,#c9d1d8)}
.diagram.new{left:400px;top:200px;width:380px;height:260px;background:linear-gradient(180deg,#edf6e4,#c6d6b9)}
.arrow-svg{position:absolute;left:330px;top:250px}
.warning{position:absolute;left:110px;top:440px;width:210px;text-align:center;color:var(--red);
  font-weight:900;font-size:18px}
</style>
</head>
<body>
<div class="poster">
  <div class="hero-photo" role="img" aria-label="既存の空洞ブロック塀と住宅の写真"></div>
  <div class="hero-shade"></div>

  <div class="tagline">まったく新しいコンクリート塀</div>
  <div class="product-name">Plim!</div>
  <div class="new-badge">新<br>製品</div>

  <div class="headline">人災が発生してからでは遅い。<br>今一度、家の塀を見直して下さい。</div>

  <p class="intro">通常、家の周りに設置する塀は空洞ブロックを積上げて構築しますが、新製品『Plim!』はこれを一体化した構造で工場で製造する1枚の<em>大きな安全性の高いコンクリート塀</em>です。</p>

  <div class="issues-title">現在起きている問題点とは</div>
  <ol class="issues">
    <li class="issue"><span class="issue-num">1</span><span class="issue-text">空洞ブロック積上げ式のブロック塀では、地震時の損壊・転倒による人災が多数発生している現状</span></li>
    <li class="issue"><span class="issue-num">2</span><span class="issue-text">材料が安価なため利用されていますが、施工基準に基づかない方法で安易に構築されるケースも多いのが実状</span></li>
    <li class="issue"><span class="issue-num">3</span><span class="issue-text">鉄筋挿入部のコンクリートの充填もルーズになりがちなため、鉄筋の酸化によりブロック塀の劣化も早くなる</span></li>
    <li class="issue"><span class="issue-num">4</span><span class="issue-text">土圧を支えきれないと思われる擁壁としての使用も多く見受けられる</span></li>
    <li class="issue"><span class="issue-num">5</span><span class="issue-text">地震時のみならず、平常時においてもブロック塀の傾き・転倒等の危険な状況が多く発生している</span></li>
  </ol>

  <div class="solution-band">新製品「Plim」で今まで起こっていた問題は解決致します!!</div>

  <section class="solution-panel">
    <p class="solution-text">今回の新製品では弊社工場内での厳格な設計基準、検査基準、安定計算の下で一体化された製品を使用するため、躯体の劣化、破損、転倒を防止することができ、平常時、地震時においても人災を免れることが可能となります。</p>

    <div class="method-label old">従来の<br>方法</div>
    <div class="diagram old" role="img" aria-label="従来の空洞ブロック塀の断面図"></div>
    <div class="warning">くずれやすくなる</div>

    <svg class="arrow-svg" width="60" height="40" viewBox="0 0 60 40" aria-hidden="true">
      <polygon points="0,12 36,12 36,2 58,20 36,38 36,28 0,28" fill="#6cb72f"/>
    </svg>

    <div class="method-label new">安全性の高い<br>新製品Plimの<br>方法</div>
    <div class="diagram new" role="img" aria-label="新製品Plimの一体化構造の断面図"></div>
  </section>
</div>
</body>
</html>
```